Commercial printing and sign company printed advertisement.

We're wanting a new look for our printed advertisements. We've been in business for 40 years and have been pushing hard the last couple of years to grow our business. Our target market is changing and our client base is changing. I am looking for advertisement that appeals to larger companies. However, we are not stuffy people so I would like the ads to convey our professionalism but also stand out with color and have a fun side. I'm currently needing advertisements for a printed magazine, printed newspaper, web ads and a table top at a local restaurant. We have our traditional four color logo (swoosh) as well as a simpler single color option. I am attaching various ads we have done previously so you can see what we have. It is important for these ads to convey the different things we do - as we do alot!

```html
<!DOCTYPE html>
<html lang="en">
<head>
<meta charset="utf-8">
<title>R&amp;K Printing – 40th Year Advertisement</title>
<link rel="stylesheet" href="https://fonts.googleapis.com/css2?family=Montserrat:wght@700;800&family=PT+Sans:wght@400&display=swap">
<style>
  :root {
    --backdrop: #55585b;
    --white: #ffffff;
    --ink: #141112;
    --red: #d50d0d;
    --red-deep: #9c0404;
    --yellow: #ede51c;
    --cyan: #1b9ad6;
    --magenta: #e4087c;
  }
  * { margin: 0; padding: 0; box-sizing: border-box; }
  html, body { width: 903px; height: 1200px; overflow: hidden; }
  body {
    background: var(--backdrop);
    font-family: "Montserrat", Arial, sans-serif;
    position: relative;
  }
  .ad-card {
    position: absolute;
    left: 21px;
    top: 294px;
    width: 860px;
    height: 612px;
    background: var(--red);
    box-shadow: 4px 6px 10px rgba(0,0,0,.35);
    display: flex;
    flex-direction: column;
    overflow: hidden;
  }
  .red-gradient {
    background: linear-gradient(90deg, var(--red-deep) 0%, var(--red) 45%, var(--red) 60%, var(--red-deep) 100%);
  }
  .brand-bar {
    height: 155px;
    flex: none;
    background: var(--white);
    display: flex;
    align-items: center;
    justify-content: center;
  }
  .brand-name {
    font-weight: 800;
    font-size: 96px;
    line-height: 1;
    color: var(--ink);
    letter-spacing: -1px;
  }
  .tagline-bar {
    height: 114px;
    flex: none;
    display: flex;
    justify-content: center;
    padding-top: 22px;
  }
  .tagline {
    font-family: "PT Sans", Arial, sans-serif;
    font-size: 44px;
    color: var(--white);
    letter-spacing: -0.5px;
    line-height: 1;
  }
  .service-band {
    flex: none;
    display: flex;
    align-items: center;
    justify-content: center;
    font-weight: 700;
    font-size: 26px;
    color: var(--white);
    white-space: nowrap;
    line-height: 1;
  }
  .service-band.yellow { height: 33px; background: var(--yellow); color: var(--ink); justify-content: space-between; padding: 0 38px 0 30px; }
  .service-band.cyan { height: 36px; background: var(--cyan); gap: 28px; }
  .service-band.magenta { height: 35px; background: var(--magenta); gap: 20px; }
  .service-band.black { height: 35px; background: var(--ink); }
  .gap { height: 4px; flex: none; }
  .item { display: inline-flex; align-items: center; gap: 9px; }
  .bullet {
    width: 16px; height: 16px; border-radius: 50%;
    background: var(--white);
    display: inline-block;
  }
  .celebration-bar {
    height: 73px;
    flex: none;
    display: flex;
    align-items: center;
    justify-content: center;
    font-weight: 800;
    font-size: 38px;
    color: var(--white);
    letter-spacing: .5px;
  }
  .stripe { height: 8px; flex: none; }
  .stripe.yellow { background: var(--yellow); }
  .stripe.cyan { background: var(--cyan); }
  .stripe.magenta { background: var(--magenta); height: 9px; }
  .contact-bar {
    flex: 1;
    background: var(--ink);
    display: flex;
    flex-direction: column;
    align-items: center;
    justify-content: center;
    gap: 4px;
    font-weight: 700;
    font-size: 30px;
    line-height: 1.1;
  }
  .contact-web { color: var(--yellow); }
  .contact-address { color: var(--cyan); }
</style>
</head>
<body>
  <article class="ad-card">
    <header class="brand-bar">
      <span class="brand-name">R&amp;K Printing</span>
    </header>

    <section class="tagline-bar red-gradient">
      <p class="tagline">A PRINTING &amp; SIGN COMPANY</p>
    </section>

    <div class="service-band yellow">
      <span class="item"><i class="bullet"></i>PRINTING</span>
      <span class="item"><i class="bullet"></i>SIGNS</span>
      <span class="item"><i class="bullet"></i>BANNERS</span>
      <span class="item"><i class="bullet"></i>POSTERS</span>
      <span class="item"><i class="bullet"></i>DECALS</span>
    </div>
    <div class="gap"></div>
    <div class="service-band cyan">
      <span class="item"><i class="bullet"></i>DESIGN</span>
      <span class="item"><i class="bullet"></i>SCREEN PRINTING</span>
      <span class="item"><i class="bullet"></i>EMBROIDERY</span>
    </div>
    <div class="gap"></div>
    <div class="service-band magenta">
      <span class="item">BLUE PRINTS</span>
      <span class="item"><i class="bullet"></i>PROMOTIONAL ITEMS</span>
    </div>
    <div class="gap"></div>
    <div class="service-band black">&amp; SO MUCH MORE!!</div>

    <section class="celebration-bar red-gradient">40TH YEAR CELEBRATION</section>

    <div class="stripe yellow"></div>
    <div class="stripe cyan"></div>
    <div class="stripe magenta"></div>

    <footer class="contact-bar">
      <span class="contact-web">WWW.RKPRINTSHOP.COM</span>
      <span class="contact-address">2210 N. MAIN ST | MAPLE RIDGE, MO</span>
    </footer>
  </article>
</body>
</html>
```